Educational Management System User Interface (Vantro Design Concepts)

Hi,I require a 1-page design for an educational management system. The image attached shows all required elements and also their locations. I require the design to be based on vantro-styled interfaces using elements from: http://qelvo.hostrun.io/qelvo-kitset/ & http://layoutmintly.com/layout-template/admin . Side menu's should not be too large that they hide the main content of the page.
Sorry very slight addition to the design as per new uploaded file.
I like how the elements of the vantro hub page are seperated with the background colour and white boxes. This could maybe work in the design as per the uploaded image?
Thanks,
Melvin
Reason: Some designers have some submissions.

```html
<!DOCTYPE html>
<html lang="en">
<head>
<meta charset="utf-8">
<title>KL LMS – Group Discussion</title>
<link rel="stylesheet" href="https://fonts.googleapis.com/css2?family=Open+Sans:wght@400;600;700&display=swap">
<style>
:root{
  --brand:#1c70b0;
  --brand-light:#2e8fdc;
  --accent:#f47a50;
  --ink:#333;
  --muted:#777;
  --side:#efefef;
  --panel:#f3f3f3;
  --head-grey:#d6d6d6;
  --line:#cfcfcf;
  --white:#fff;
}
*{box-sizing:border-box;margin:0;padding:0}
html,body{width:1200px;height:1028px;overflow:hidden;background:var(--white);font-family:"Open Sans",Arial,sans-serif;color:var(--ink)}
.app{position:relative;width:1200px;height:1028px}
.abs{position:absolute}
.topbar{left:0;top:0;width:1200px;height:90px;background:var(--brand)}
.brand{left:30px;top:0;height:90px;display:flex;align-items:center;gap:12px;color:var(--white);font-size:34px;font-weight:600;letter-spacing:.5px}
.brand .dot{width:30px;height:30px;border-radius:50%;background:var(--white)}
.nav-home{left:261px;top:0;width:81px;height:90px;background:var(--brand-light)}
.nav-icon{top:30px}
.user-tab{left:970px;top:0;width:230px;height:90px;background:var(--brand-light);display:flex;align-items:center;gap:12px;padding-left:18px;color:var(--white);font-weight:700;font-size:16px}
.badge{position:absolute;width:13px;height:13px;border-radius:50%;background:var(--accent);color:#fff;font-size:9px;font-weight:700;text-align:center;line-height:13px}

.sidebar{left:0;top:90px;width:261px;height:938px;background:var(--side)}
.role{left:0;top:90px;width:261px;height:64px;background:var(--white);box-shadow:0 3px 4px rgba(0,0,0,.06);color:var(--brand);font-weight:700;font-size:21px;padding:20px 0 0 71px}
.section-title{color:var(--brand);font-weight:700;font-size:19px;left:70px}
.group-item{left:0;width:261px;height:45px;display:flex;align-items:center;padding-left:69px;font-size:16px;color:#555;border-bottom:1px solid #e4e4e4}
.group-item.active{background:var(--white);color:var(--brand)}
.group-item .chev{position:absolute;right:22px;color:#aaa;font-size:14px}
.group-item.active .chev{color:var(--accent)}
.side-btn{left:15px;width:237px;height:45px;border:1px solid #b5b5b5;background:#f7f7f7;box-shadow:0 1px 2px rgba(0,0,0,.15);font-weight:600;font-size:16px;text-align:center;line-height:43px;color:#222}

.crumbs{left:287px;top:150px;display:flex;gap:26px;align-items:center;color:var(--brand);font-size:18px;font-weight:600}
.crumbs .sep{font-size:10px}
.hint{left:287px;top:190px;font-size:14px;color:#666}
.resources{left:284px;top:226px;width:661px;height:123px;border:1px solid #ddd;background:var(--white)}
.res-tab{top:18px;width:90px;text-align:center;font-size:13px;color:#888}
.res-tab .box{width:68px;height:56px;margin:0 auto 10px;border:1px solid #e2e2e2;background:#fafafa;display:flex;align-items:center;justify-content:center}
.res-tab.active{color:var(--brand);font-weight:600}
.res-tab.active .box{border-color:#b9d3ea;background:#fff}

.avatar-me{left:290px;top:390px;width:56px;height:56px;border-radius:50%;border:1px solid #b9d3ea;display:flex;align-items:center;justify-content:center}
.update{left:369px;top:396px;width:576px;height:45px;background:#eee;border:1px solid #999;padding:14px 0 0 23px;font-size:13px;color:#333}
.submit{left:834px;top:452px;width:110px;height:38px;border:1px solid #b5b5b5;background:#f8f8f8;box-shadow:0 1px 2px rgba(0,0,0,.15);text-align:center;line-height:36px;font-weight:600;font-size:15px}
.timeline{left:318px;width:2px;background:var(--line)}
.post{left:370px;width:574px;background:var(--panel);padding:30px 25px 0 23px}
.post-head{display:flex;justify-content:space-between;color:var(--brand);font-size:12.5px;font-weight:600;margin-bottom:22px;padding-right:0}
.post p{font-size:13px;line-height:23.5px;color:#333}
.share{right:3px;bottom:3px;width:42px;height:36px;background:var(--white);display:flex;align-items:center;justify-content:center}
.share.dim{background:#e3e3e3}
.photo{border-radius:50%;background:linear-gradient(#9a8c80,#4c4642);border:1px solid #e7b8a5}

.rightbar{left:970px;top:90px;width:230px;height:855px;background:#eeeeee}
.rb-head{left:970px;width:230px;background:var(--head-grey);display:flex;align-items:center;gap:12px;padding-left:14px;color:#666;font-weight:700;font-size:17px;box-shadow:0 3px 4px rgba(0,0,0,.08)}
.member{left:983px;display:flex;align-items:center;gap:13px;font-size:13px;color:#222}
.member .pic{position:relative;width:56px;height:52px;background:linear-gradient(#c8b8a8,#6d6058);border:1px solid #ddd}
.member .dot{position:absolute;right:-5px;bottom:-5px;width:12px;height:12px;border-radius:50%;border:2px solid var(--accent);background:#fff}
.loadlist{left:970px;top:597px;width:230px;height:33px;background:var(--white);font-size:12px;padding:9px 0 0 120px}
.event{left:978px;display:flex;align-items:center;font-size:13px;color:#333}
.event .time{width:34px;height:27px;background:#fff;display:flex;align-items:center;justify-content:center;font-size:12px}
.event .ap{width:26px;height:27px;background:#9d9d9d;color:#fff;font-size:10px;display:flex;align-items:center;justify-content:center;margin-right:6px}
.event.now .ap{background:var(--accent)}
.event.now .label{color:var(--brand);font-weight:700}
.leave{left:970px;top:963px;width:218px;height:41px;border:1px solid #bbb;background:#f6f6f6;display:flex;align-items:center;gap:8px;padding-left:10px;font-weight:600;font-size:14px}
</style>
</head>
<body>
<div class="app">
  <header class="abs topbar"></header>
  <div class="abs brand"><span class="dot"></span>KL LMS</div>
  <div class="abs nav-home"></div>
  <svg class="abs nav-icon" style="left:288px" width="27" height="28" viewBox="0 0 27 28" fill="none" stroke="#fff" stroke-width="2"><path d="M2 13L13.5 3 25 13M5 11v15h17V11M11 26v-8h5v8"/></svg>
  <svg class="abs nav-icon" style="left:368px" width="24" height="26" viewBox="0 0 24 26" fill="none" stroke="#fff" stroke-width="2"><rect x="1" y="4" width="22" height="21"/><path d="M6 1v6M18 1v6M1 10h22"/><path d="M5 14h14M5 18h14M5 22h14" stroke-width="1.5" stroke-dasharray="2 2"/></svg>
  <svg class="abs nav-icon" style="left:429px" width="28" height="26" viewBox="0 0 28 26" fill="none" stroke="#fff" stroke-width="3.5"><path d="M2 14l8 9L26 2"/></svg>
  <svg class="abs nav-icon" style="left:492px" width="28" height="24" viewBox="0 0 28 24" fill="#fff"><path d="M0 4h10l3 3h15v17H0z"/></svg>
  <svg class="abs" style="left:881px;top:34px" width="24" height="26" viewBox="0 0 24 26" fill="#fff"><path d="M12 2c-5 0-7 4-7 8v6l-3 4h20l-3-4v-6c0-4-2-8-7-8zM9 22a3 3 0 006 0z"/></svg>
  <span class="badge" style="left:896px;top:32px">1</span>
  <svg class="abs" style="left:925px;top:38px" width="30" height="20" viewBox="0 0 30 20" fill="#fff" stroke="#1c70b0" stroke-width="1.3"><rect x=".5" y=".5" width="29" height="19"/><path d="M.5 .5L15 12 29.5 .5M.5 19.5L11 9M29.5 19.5L19 9" fill="none"/></svg>
  <span class="badge" style="left:948px;top:32px">1</span>
  <div class="abs user-tab"><svg width="24" height="26" viewBox="0 0 24 26" fill="#fff"><circle cx="12" cy="8" r="6"/><path d="M1 25c0-7 5-10 11-10s11 3 11 10z"/></svg>DELIA FENWICK</div>

  <aside class="abs sidebar"></aside>
  <div class="abs role">TEACHER</div>
  <div class="abs section-title" style="top:183px">MY GROUPS</div>
  <div class="abs group-item active" style="top:227px">
    <svg style="position:absolute;left:30px" width="24" height="22" viewBox="0 0 24 22" fill="#f47a50"><circle cx="9" cy="6" r="5"/><path d="M0 21c0-6 4-9 9-9s9 3 9 9zM17 12l6 4-3 2z"/></svg>
    Group Name One<span class="chev">»</span></div>
  <div class="abs group-item" style="top:280px">Group Name Two<span class="chev">»</span></div>
  <div class="abs group-item" style="top:332px">Group&nbsp; Name Three<span class="chev">»</span></div>
  <div class="abs group-item" style="top:384px">Group&nbsp; Name Four<span class="chev">»</span></div>
  <div class="abs side-btn" style="top:458px">CREATE NEW GROUP</div>
  <div class="abs side-btn" style="top:522px">JOIN MORE GROUPS</div>
  <div class="abs section-title" style="top:614px;font-size:21px">COMMUNITY</div>
  <div class="abs group-item" style="top:662px">Study Nook<span class="chev">»</span></div>

  <nav class="abs crumbs"><span>MY GROUPS</span><span class="sep">▶</span><span>THE MARLOWE GROUP</span><span class="sep">▶</span><span>DISCUSSION</span></nav>
  <svg class="abs" style="left:918px;top:158px" width="24" height="24" viewBox="0 0 24 24" fill="#999"><rect x="0" y="0" width="6" height="6"/><rect x="9" y="0" width="6" height="6"/><rect x="18" y="0" width="6" height="6"/><rect x="0" y="9" width="6" height="6"/><rect x="9" y="9" width="6" height="6"/><rect x="18" y="9" width="6" height="6"/><rect x="0" y="18" width="6" height="6"/><rect x="9" y="18" width="6" height="6"/><rect x="18" y="18" width="6" height="6"/></svg>
  <div class="abs hint">Group Resources Dropdown Box (Starts minimized)</div>

  <section class="abs resources">
    <div class="abs res-tab active" style="left:11px"><div class="box"><svg width="46" height="34" viewBox="0 0 46 34" fill="#f47a50"><ellipse cx="17" cy="13" rx="16" ry="11"/><path d="M8 21l-4 8 10-5z"/><ellipse cx="31" cy="18" rx="13" ry="9" stroke="#fff" stroke-width="2"/><path d="M38 25l5 7-10-4z"/></svg></div>Discussion</div>
    <div class="abs res-tab" style="left:105px"><div class="box"><svg width="28" height="34" viewBox="0 0 28 34" fill="none" stroke="#bbb" stroke-width="2"><rect x="1" y="1" width="26" height="32"/><path d="M6 9h16M6 14h16M6 19h16M6 24h16"/></svg></div>Assignments</div>
    <div class="abs res-tab" style="left:199px"><div class="box"><svg width="34" height="32" viewBox="0 0 34 32" fill="#bbb"><text x="0" y="21" font-size="16" font-family="Open Sans">?</text><rect x="12" y="2" width="20" height="4"/><rect x="12" y="10" width="20" height="4"/><rect x="12" y="18" width="20" height="4"/><rect x="12" y="26" width="20" height="4"/></svg></div>Quizzes</div>
    <div class="abs res-tab" style="left:291px"><div class="box"><svg width="32" height="30" viewBox="0 0 32 30" fill="#bbb"><rect x="3" y="16" width="4" height="11"/><rect x="10" y="9" width="4" height="18"/><rect x="17" y="3" width="4" height="24"/><rect x="24" y="12" width="4" height="15"/><rect x="0" y="28" width="32" height="2"/></svg></div>Polls</div>
    <div class="abs res-tab" style="left:380px"><div class="box"><svg width="28" height="34" viewBox="0 0 28 34" fill="#f6f6f6" stroke="#bbb" stroke-width="1.6"><rect x="9" y="1" width="18" height="24"/><rect x="5" y="5" width="18" height="24"/><rect x="1" y="9" width="18" height="24"/><path d="M5 16h10M5 21h10M5 26h10"/></svg></div>Files</div>
    <div class="abs res-tab" style="left:469px"><div class="box"><svg width="30" height="32" viewBox="0 0 30 32" fill="#bbb"><circle cx="15" cy="12" r="10"/><path d="M8 19l-4 10 6-2 3 4 2-9zM22 19l4 10-6-2-3 4-2-9z"/></svg></div>Badges</div>
    <div class="abs res-tab" style="left:565px"><div class="box"><svg width="24" height="32" viewBox="0 0 24 32" fill="#bbb"><rect x="6" y="1" width="12" height="16" rx="3"/><rect x="2" y="18" width="20" height="4"/><rect x="11" y="22" width="2" height="6"/><rect x="5" y="28" width="14" height="2"/></svg></div>Seating Plan</div>
  </section>
  <svg class="abs" style="left:633px;top:347px" width="10" height="6" viewBox="0 0 10 6" fill="#1c70b0"><path d="M0 0h10L5 6z"/></svg>

  <div class="abs avatar-me"><svg width="26" height="28" viewBox="0 0 26 28" fill="#f47a50"><circle cx="13" cy="8" r="7"/><path d="M0 27c0-7 6-11 13-11s13 4 13 11z"/></svg></div>
  <div class="abs update">Please post your update...</div>
  <svg class="abs" style="left:725px;top:477px" width="24" height="14" viewBox="0 0 24 14" fill="none" stroke="#999" stroke-width="2"><rect x="1" y="3" width="12" height="8" rx="4"/><rect x="11" y="3" width="12" height="8" rx="4"/></svg>
  <svg class="abs" style="left:765px;top:474px" width="14" height="17" viewBox="0 0 14 17" fill="none" stroke="#999" stroke-width="1.6"><path d="M1 1h8l4 4v11H1z"/></svg>
  <svg class="abs" style="left:797px;top:474px" width="22" height="17" viewBox="0 0 22 17" fill="#999"><path d="M0 4h5l2-3h8l2 3h5v13H0z"/><circle cx="11" cy="10" r="4" fill="#fff"/></svg>
  <div class="abs submit">SUBMIT</div>

  <svg class="abs" style="left:303px;top:482px" width="30" height="32" viewBox="0 0 30 32" fill="none" stroke="#999" stroke-width="3"><path d="M8 24A11 11 0 1122 24"/><circle cx="15" cy="28" r="3" fill="#999" stroke="none"/></svg>
  <div class="abs timeline" style="top:522px;height:68px"></div>
  <div class="abs timeline" style="top:680px;height:120px"></div>
  <div class="abs timeline" style="top:892px;height:52px"></div>

  <article class="abs post" style="top:539px;height:192px">
    <div class="post-head"><span>ROWAN KEELEY</span><span>9.15 &nbsp;I&nbsp; 14/05/2014</span></div>
    <p>Lorem profile dolor sit amet, consectetur adipiscing elit. Duis pharetra varius quam sit amet vulputate. Quisque mauris augue, molestie tincidunt condimentum vitae, gravida a libero. Aenean sit amet felis dolor, in sagittis nisi.</p>
    <div class="abs share"><svg width="24" height="18" viewBox="0 0 24 18" fill="none" stroke="#1c70b0" stroke-width="2.5"><path d="M9 4H2v12h19M15 12l5-5-5-5M20 7v6"/></svg></div>
  </article>
  <div class="abs photo" role="img" aria-label="Profile photo of Rowan Keeley" style="left:290px;top:608px;width:56px;height:56px"></div>

  <article class="abs post" style="top:751px;height:193px">
    <div class="post-head"><span>ROWAN KEELEY</span><span>9.15 &nbsp;I&nbsp; 14/05/2014</span></div>
    <p>Lorem profile dolor sit amet, consectetur adipiscing elit. Duis pharetra varius quam sit amet vulputate. Quisque mauris augue, molestie tincidunt condimentum vitae, gravida a libero. Aenean sit amet felis dolor, in sagittis nisi.</p>
    <div class="abs share dim"><svg width="24" height="18" viewBox="0 0 24 18" fill="none" stroke="#fff" stroke-width="2.5"><path d="M9 4H2v12h19M15 12l5-5-5-5M20 7v6"/></svg></div>
  </article>
  <div class="abs photo" role="img" aria-label="Profile photo of group member" style="left:290px;top:819px;width:56px;height:56px"></div>

  <aside class="abs rightbar"></aside>
  <div class="abs rb-head" style="top:92px;height:62px"><svg width="38" height="24" viewBox="0 0 38 24" fill="#777"><circle cx="10" cy="7" r="5"/><circle cx="28" cy="7" r="5"/><circle cx="19" cy="6" r="6"/><path d="M0 22c0-6 4-8 10-8s9 2 9 8zM19 22c0-6 4-8 9-8s10 2 10 8zM8 24c0-7 5-10 11-10s11 3 11 10z"/></svg>&nbsp;Group Members</div>
  <div class="abs member" style="top:186px"><div class="pic" role="img" aria-label="Photo of Tobin Ashcroft"><span class="dot"></span></div>Tobin Ashcroft</div>
  <div class="abs member" style="top:256px"><div class="pic" role="img" aria-label="Photo of Perry Calderwood"><span class="dot"></span></div>Perry Calderwood</div>
  <div class="abs member" style="top:324px"><div class="pic" role="img" aria-label="Photo of Niall Hargrove"></div>Niall Hargrove</div>
  <div class="abs member" style="top:390px"><div class="pic" role="img" aria-label="Photo of Ewan Pritchard"></div>Ewan Pritchard</div>
  <div class="abs member" style="top:456px"><div class="pic" role="img" aria-label="Photo of Owen Tarrant"></div>Owen Tarrant</div>
  <div class="abs member" style="top:525px"><div class="pic" role="img" aria-label="Photo of Rowan Keeley"></div>Rowan Keeley</div>
  <div class="abs loadlist">Load Full List <svg style="vertical-align:-4px;margin-left:6px" width="18" height="18" viewBox="0 0 18 18" stroke="#999" stroke-width="2"><path d="M9 1v4M9 13v4M1 9h4M13 9h4M3 3l3 3M12 12l3 3M3 15l3-3M12 6l3-3"/></svg></div>
  <div class="abs rb-head" style="top:631px;height:61px;gap:8px;padding-left:8px"><svg width="28" height="28" viewBox="0 0 28 28" fill="none" stroke="#777" stroke-width="2"><rect x="1" y="4" width="26" height="23"/><path d="M1 10h26M7 1v6M21 1v6"/><text x="10" y="24" font-size="12" fill="#777" stroke="none" font-family="Open Sans" font-weight="700">7</text></svg>Upcoming Group Events</div>
  <div class="abs event now" style="top:721px"><span class="time">12.15</span><span class="ap">AM</span><span class="label">Meeting in the Canteen</span></div>
  <div class="abs event" style="top:769px"><span class="time">12.54</span><span class="ap">PM</span><span class="label">Assignment One is due</span></div>
  <div class="abs event" style="top:814px"><span class="time">12.45</span><span class="ap">PM</span><span class="label">New Quiz in classromm 1</span></div>
  <div class="abs event" style="top:859px"><span class="time">4.15</span><span class="ap">PM</span><span class="label">Meeting int the Canteen</span></div>
  <div class="abs event" style="top:898px"><span class="time">4.15</span><span class="ap">PM</span><span class="label">Meeting int the Canteen</span></div>
  <div class="abs leave"><svg width="28" height="28" viewBox="0 0 28 28" fill="none" stroke="#999" stroke-width="2.5"><path d="M12 4H3v21h21v-9M14 14L26 2M17 2h9v9"/></svg>REQUEST TO LEAVE GROUP</div>
</div>
</body>
</html>
```